make a fireworks website

we are manufacturer of fireworks in Asia.
we need a HD fireworks website for showing product to all world customers.
we also need an register for member system,location, forum,products..etc
I added my Logo for the company.
brightpeonyhall.com.hk

and please message me if you have
any question.
here some example of website:
http://www.lanternmoth.com/
http://www.korvelmist.com/
http://www.tindle-orbwick.co.uk/
http://www.pemberlyspark.co.uk/

```html
<!DOCTYPE html>
<html lang="en">
<head>
<meta charset="utf-8">
<title>Bright Peony Hall</title>
<link rel="stylesheet" href="https://fonts.googleapis.com/css2?family=Lato:wght@100;300;400;900&family=Oswald:wght@400&family=Arimo:wght@400;700&display=swap">
<style>
  :root {
    --ink: #000000;
    --paper: #ffffff;
    --sun: #fcc70c;
    --gold: #f2c500;
    --nav-ink: #1f3d12;
    --slate: #8a909e;
    --placeholder: #808080;
    --placeholder-ink: #cfcfcf;
    --body-grey: #8a8a8a;
    --rule: #6b6b6b;
    --accent: #e0127a;
    --violet: #7a2a9c;
  }
  * { margin: 0; padding: 0; box-sizing: border-box; }
  html, body { width: 1200px; height: 1194px; overflow: hidden; background: var(--paper); }
  .page { position: relative; width: 1200px; height: 1194px; overflow: hidden; font-family: "Arimo", Arial, sans-serif; }

  .search {
    position: absolute; left: 786px; top: 17px; width: 212px; height: 29px;
    background: var(--ink); border-radius: 15px;
    color: #d6d6d6; font-size: 19px; line-height: 29px; padding-left: 11px;
  }
  .account { position: absolute; top: 11px; font-family: "Oswald", sans-serif; font-size: 27px; color: var(--ink); letter-spacing: 0.5px; }
  .account.signup { left: 1025px; }
  .account.login { left: 1125px; }

  .hero {
    position: absolute; left: 0; top: 120px; width: 1200px; height: 362px;
    background:
      radial-gradient(ellipse 260px 170px at 640px 150px, rgba(122,42,156,0.35), transparent 70%),
      radial-gradient(ellipse 220px 150px at 900px 90px, rgba(224,18,122,0.28), transparent 70%),
      radial-gradient(ellipse 200px 130px at 470px 280px, rgba(242,197,0,0.18), transparent 70%),
      var(--ink);
  }
  .masthead { position: absolute; left: 19px; top: 57px; width: 1159px; height: 72px; background: var(--sun); }
  .brand { position: absolute; left: 12px; top: 11px; display: flex; align-items: center; gap: 10px; }
  .brand-dot { width: 50px; height: 50px; border-radius: 50%; background: var(--accent); }
  .brand-name { font-family: "Lato", sans-serif; font-weight: 900; font-size: 19px; color: var(--ink); }
  .nav a { position: absolute; top: 26px; font-size: 19px; color: var(--nav-ink); text-decoration: none; }

  .promo { position: absolute; left: 41px; top: 211px; font-family: "Lato", sans-serif; font-weight: 300; font-size: 40px; line-height: 47px; color: var(--gold); }
  .slider-label { position: absolute; left: 486px; top: 272px; font-weight: 700; font-size: 19px; letter-spacing: 4px; color: var(--slate); }

  .fade-panel {
    position: absolute; left: 712px; top: 302px; width: 464px; height: 363px;
    background: radial-gradient(ellipse at 50% 45%, #8e8e8e, var(--placeholder) 60%, #6f6f6f);
  }
  .fade-panel span { position: absolute; left: 0; right: 0; top: 169px; text-align: center; font-weight: 700; font-size: 19px; letter-spacing: 3.5px; color: var(--placeholder-ink); }

  .welcome { position: absolute; left: 30px; top: 492px; font-family: "Lato", sans-serif; font-weight: 900; font-size: 29px; line-height: 35px; color: var(--ink); }
  .welcome-word {
    position: absolute; left: 26px; top: 582px; font-family: "Lato", sans-serif; font-weight: 100; font-size: 84px; line-height: 90px; letter-spacing: 1px;
    background: linear-gradient(90deg, #e8a020, #d0208a, #7a3cc0, #2a7ad8, #1a1a1a);
    -webkit-background-clip: text; background-clip: text; color: transparent;
  }

  .product {
    position: absolute; left: 25px; top: 688px; width: 688px; height: 449px;
    background:
      radial-gradient(ellipse 200px 170px at 560px 330px, rgba(224,18,122,0.30), transparent 70%),
      radial-gradient(ellipse 160px 140px at 500px 200px, rgba(122,42,156,0.28), transparent 70%),
      var(--ink);
  }
  .product-divider { position: absolute; left: 348px; top: 41px; width: 1px; height: 352px; background: var(--rule); }
  .product-desc { position: absolute; left: 42px; top: 140px; font-family: "Lato", sans-serif; font-weight: 300; font-size: 38px; line-height: 47px; color: var(--gold); }
  .product-image { position: absolute; left: 383px; top: 188px; font-size: 36px; line-height: 43px; color: #8e8e8e; }
  .product-slider { position: absolute; left: 305px; top: 415px; font-size: 17px; letter-spacing: 3.5px; color: #8a8a8a; }

  .story { position: absolute; left: 735px; top: 688px; width: 420px; }
  .story h2 { font-family: "Lato", sans-serif; font-weight: 900; font-size: 29px; line-height: 35px; color: var(--ink); margin-bottom: 24px; }
  .story p { font-size: 17.5px; line-height: 21.7px; color: var(--body-grey); margin-bottom: 21.7px; }

  .footer-note { position: absolute; left: 27px; top: 1157px; font-size: 12px; color: #1a1a4a; }
</style>
</head>
<body>
<div class="page">
  <div class="search">SEARCH</div>
  <a class="account signup">SIGN UP</a>
  <a class="account login">LOGIN</a>

  <section class="hero" role="img" aria-label="Slideshow of night-sky firework bursts"></section>

  <header class="masthead">
    <div class="brand">
      <div class="brand-dot"></div>
      <span class="brand-name">brightpeonyhall.com.hk</span>
    </div>
    <nav class="nav">
      <a style="left:605px">HOME</a>
      <a style="left:710px">PRODUCTS</a>
      <a style="left:865px">BRANCHES</a>
      <a style="left:1021px">CONTACT US</a>
    </nav>
  </header>

  <p class="promo">PROMOTIONAL<br>TEXT<br>ABOUT THE<br>COMPANY</p>
  <p class="slider-label">IMAGE&nbsp; SLIDER</p>

  <div class="fade-panel" role="img" aria-label="Rotating firework photograph"><span>IMAGE&nbsp; FADE IN/OUT</span></div>

  <h1 class="welcome">WELCOME<br>TO THE<br>GRAND WORLD OF</h1>
  <p class="welcome-word">FIREWORKS</p>

  <section class="product" role="img" aria-label="Featured firework product with description">
    <p class="product-desc">DESCRIPTION<br>&nbsp;OF<br>THIS<br>PRODUCT</p>
    <div class="product-divider"></div>
    <p class="product-image">PRODUCT<br>IMAGE</p>
    <p class="product-slider">SLIDER</p>
  </section>

  <section class="story">
    <h2>HEADER<br>FOR THE<br>TEXT BELOW</h2>
    <p>Text describing the company. Text describing the company. Text describing the company. Text describing the company. Text describing the company. Text describing the company.<br>Text describing the company. Text describing the company.</p>
    <p>Text describing the company. Text describing the company.</p>
    <p>Text describing the company. Text describing the company. Text describing the company. Text describing the company. Text describing the company.</p>
  </section>

  <p class="footer-note">Copyright etc.</p>
</div>
</body>
</html>
```